Consultancy Business Card Design

We need a business card design for a new company based in singapore called FortyOne. FortyOne a boutique consultancy firm offering broad-based business solutions, from conception to re-invention, for ventures from new start-ups to long-running traditional businesses.
Its 2 main divisions (Food & Beverage Operations and Construction & Project Management) have access to a wide range of networks, knowledge bases, and resources to service its clients across numerous diverse sectors. This includes, and is not limited to, construction, F&B, and retail.
We are a company that combines the ambition, boldness and energy of one in the 20s with the dedication, level-headedness and dependability of one entering its 30s. Bridging the experiences of the old with ideals of the young, we draw on the positives of both to create a unique synergy.
We hope to see designs that fits our company profile.
Boutique
FortyOne(Company Name)
Marcus Leow (Name)
Principle Consultant (Title)
F&B and Hospitality (Division)
(+65) 8364 5170 (Contact no.)
marcus@fortyone-example.com.sg (Email)

```html
<!DOCTYPE html>
<html lang="en">
<head>
<meta charset="utf-8">
<title>FortyOne — Business Card</title>
<link rel="stylesheet" href="https://fonts.googleapis.com/css2?family=Alegreya+Sans+SC:wght@500;800&family=Open+Sans:wght@400&display=swap">
<style>
  :root {
    --bg: #e4e4e4;
    --card-white: #ffffff;
    --ink: #2a2a2a;
    --panel-dark: #4b4b4d;
    --panel-light: #c9c9ca;
    --border-dark: #3d3d3f;
    --accent-orange: #f7a12b;
    --text-light: #ffffff;
    --shadow: 0 6px 18px rgba(0,0,0,0.18);
  }
  * { margin: 0; padding: 0; box-sizing: border-box; }
  html, body {
    width: 1200px; height: 900px; overflow: hidden;
    background: var(--bg);
  }
  .canvas { position: relative; width: 1200px; height: 900px; }

  .card {
    position: absolute;
    width: 620px; height: 354px;
    background: var(--card-white);
    box-shadow: var(--shadow);
    overflow: hidden;
  }

  /* Back of card */
  .card--back {
    left: 60px; top: 50px;
    border: 14px solid var(--border-dark);
  }
  .card--back .frame {
    position: absolute; inset: 0;
    border: 11px solid var(--accent-orange);
    display: flex; align-items: center; justify-content: center;
  }
  .wordmark {
    font-family: "Alegreya Sans SC", sans-serif;
    font-weight: 800;
    color: var(--ink);
    letter-spacing: -1px;
    line-height: 1;
  }
  .card--back .wordmark { font-size: 118px; }

  /* Front of card */
  .card--front { left: 520px; top: 496px; }
  .card--front .bands { position: absolute; inset: 0; }
  .card--front .wordmark {
    position: absolute; left: 0; right: 0; top: 28px;
    text-align: center; font-size: 92px;
    padding-left: 40px;
  }

  .identity {
    position: absolute; left: 24px; top: 158px;
    font-family: "Alegreya Sans SC", sans-serif;
    font-weight: 500;
    color: var(--text-light);
    line-height: 1.05;
  }
  .identity .person { font-size: 29px; letter-spacing: 0.5px; }
  .identity .role { font-size: 19px; letter-spacing: 0.6px; }

  .contact {
    position: absolute;
    display: flex; align-items: center; gap: 10px;
    font-family: "Open Sans", sans-serif;
    font-size: 18px; color: var(--ink);
    letter-spacing: 0.6px;
    line-height: 1.2;
  }
  .contact svg { width: 18px; height: 18px; fill: var(--ink); flex: none; }
  .contact--phone { left: 340px; top: 196px; }
  .contact--email { left: 262px; top: 290px; font-size: 17px; }
</style>
</head>
<body>
<main class="canvas">

  <section class="card card--back" aria-label="Card back">
    <div class="frame">
      <span class="wordmark">FortyOne</span>
    </div>
  </section>

  <section class="card card--front" aria-label="Card front">
    <svg class="bands" viewBox="0 0 620 354" width="620" height="354" aria-hidden="true">
      <rect x="0" y="150" width="620" height="204" fill="var(--panel-dark)"/>
      <polygon points="308,162 620,162 620,354 200,354" fill="var(--text-light)"/>
      <polygon points="316,168 620,168 620,354 210,354" fill="var(--panel-light)"/>
      <rect x="0" y="246" width="620" height="14" fill="var(--accent-orange)"/>
    </svg>

    <span class="wordmark">FortyOne</span>

    <div class="identity">
      <div class="person">Marcus Leow</div>
      <div class="role">Principle Consultant</div>
      <div class="role">F&amp;B and Hospitality</div>
    </div>

    <div class="contact contact--phone">
      <svg viewBox="0 0 24 24" aria-hidden="true"><path d="M6.6 10.8a15.1 15.1 0 0 0 6.6 6.6l2.2-2.2c.3-.3.7-.4 1-.2 1.1.4 2.3.6 3.6.6.6 0 1 .4 1 1V20c0 .6-.4 1-1 1A17 17 0 0 1 3 4c0-.6.4-1 1-1h3.5c.6 0 1 .4 1 1 0 1.3.2 2.5.6 3.6.1.3 0 .7-.2 1l-2.3 2.2z"/></svg>
      <span>(+65) 8364 5170</span>
    </div>

    <div class="contact contact--email">
      <svg viewBox="0 0 24 24" aria-hidden="true"><path d="M2 5h20v14H2V5zm2 2v.4l8 5.2 8-5.2V7H4zm16 2.8-8 5.2-8-5.2V17h16V9.8z"/></svg>
      <span>marcus@fortyone-example.com.sg</span>
    </div>
  </section>

</main>
</body>
</html>
```